Flyer Design Project

*Update* Would also be interested to see designs in landscape format too.
My company is Brenwick Van Hire Limited. A self drive van hire company based in Essex.
I need a double sided A5 flyer design to target new business customers both small and large. The flyer will be printed on 350-400gsm.
Our website is www.brenwickvanhire.example this will give you an idea of our colour scheme.
The purpose of the flyer is to make companies aware of our business and what we offer and to ideally either make contact with us immediatly or at least retain the flyer so that they use us in future. Our aim is that when they require van hire they think of us first.
In terms of design it needs to be proffessional, eye catching, informative and memorable.
I would like the 4 main van types we supply to be on the leaflet. ideally side views. Probably stock images with our graphics placed on them. I'm sure as a designer you will have a fair idea of what I'm talking about. The van types are Mercer link, Mercer SWB, Mercer LWB high roof and Mercer luton.
Our facebook page may also help (pictures of some of our vans are here)...
http://www.facebook.example/pages/Brenwick-Van-Hire/508273619402
Ideally it will include the following. The layout of the content however I am happy to leave to the designer...
(title) Low cost business van hire
Throughout Essex and Herts including Harlow, Epping, Hoddesdon, Bishops Stortford and Hertford
We have vans in all sizes including Luton tail lifts for short and long term rental on flexible terms for any purpose at very competitive prices.
Open 7 days
Short or long term rental on daily, weekly or monthly payment terms
No charges for additional drivers
Unlimited mileage allowance
24/7 online booking facility
Account facilities available
Secure customer parking
Out of hours drop off facility
(maybe use tick boxes for the above?)
When you need a van for business purposes give Brenwick a call first.
We supply vans to businesses throughout Herts and Essex from large blue chip multinationals to small self employed tradesman. We understand the requirements of business customers and provide a low cost, flexible, efficient van hire solution regardless of the size of your business.
We’re cheaper than the rest
We regularly search the market to ensure our pricing is always competitive. It's important to us to give you excellent value for money. We operate a clear pricing structure with no hidden extras. Call us now and let us give you a quote.
Short or long term van hire
We can supply vans according to your needs from just a single days rental to long term contract rental for 1 month, 6 months, a whole year or more.
Committed to Customer service
We take customer service very seriously. We want you to be delighted each and every time you use us. That’s why We’ll always go out of our way to give you a first class service.
The longer you hire the cheaper it gets with discounts of up to 70% on our daily rental rates. (maybe in speech type bubble or highlighted in some way?)
Flyer needs:
Map of our location and address
- Finding us is easy, we're located in the foxmead industrial estate in Harlow
42 Tanwell Court
Harlow
Essex
CM17 2QT
Telephone number
0800 06 317 94
Website address
www.brenwickvanhire.example
Logo
attached
Testimonial?
Can supply
www.brenwickvanhire.example
0800 06 317 94

```html
<!DOCTYPE html>
<html lang="en">
<head>
<meta charset="utf-8">
<title>Brenwick Van Hire – Business Flyer</title>
<link rel="stylesheet" href="https://fonts.googleapis.com/css2?family=Arimo:ital,wght@0,400;0,700;1,400;1,700&display=swap">
<style>
  :root {
    --lime: #66cc00;
    --banner-top: #93c782;
    --banner-bottom: #4f8f45;
    --banner-edge: #3d6f35;
    --ink: #111111;
    --map-frame: #5a9a4a;
    --map-fill: #e9e6df;
    --arrow: #f5f000;
    --arrow-edge: #d8d200;
    --tick-icon: #6f7f6a;
    --paper: #ffffff;
  }
  * { margin: 0; padding: 0; box-sizing: border-box; }
  html, body { width: 847px; height: 1200px; overflow: hidden; background: var(--paper); }
  body { font-family: "Arimo", Arial, sans-serif; color: var(--ink); }
  .flyer { position: relative; width: 847px; height: 1200px; overflow: hidden; background: var(--paper); }
  .backdrop { position: absolute; inset: 0; }
  .top-band { position: absolute; left: 0; top: 0; width: 847px; height: 42px; background: var(--lime); }
  .copy { position: absolute; font-size: 17.5px; line-height: 22px; }
  .intro { left: 103px; top: 64px; width: 720px; }
  .lead { left: 103px; top: 228px; width: 720px; }
  .banner { position: absolute; left: 36px; width: 811px; height: 82px; }
  .banner svg { position: absolute; inset: 0; }
  .banner-text { position: absolute; left: 0; width: 560px; color: #fff; font-size: 22px; line-height: 27px; text-align: center; font-weight: 400; }
  .banner-call { top: 112px; }
  .banner-call .banner-text { top: 16px; }
  .banner-discount { top: 704px; }
  .banner-discount .banner-text { top: 16px; width: 570px; }
  .point { position: absolute; left: 52px; width: 780px; }
  .point-icon { position: absolute; left: 0; top: 2px; width: 46px; height: 26px; }
  .point-title { margin-left: 51px; font-size: 23px; font-weight: 700; font-style: italic; text-decoration: underline; line-height: 28px; }
  .point-body { margin-left: 51px; font-size: 17.5px; line-height: 22px; }
  .point-price { top: 341px; }
  .point-term { top: 484px; }
  .point-service { top: 582px; }
  .tagline { position: absolute; left: 52px; top: 838px; font-size: 41px; line-height: 51px; font-weight: 400; }
  .tagline em { font-style: italic; }
  .address { position: absolute; left: 52px; top: 1020px; font-size: 23px; line-height: 28px; }
  .phone { position: absolute; left: 50px; top: 1086px; font-size: 29px; line-height: 34px; }
  .website { position: absolute; left: 50px; top: 1128px; font-size: 46px; line-height: 54px; white-space: nowrap; }
  .map { position: absolute; left: 527px; top: 799px; width: 266px; height: 260px; border: 4px solid var(--map-frame); background: linear-gradient(160deg, #f1efe9, var(--map-fill)); }
  .gps { position: absolute; left: 529px; top: 1068px; font-size: 16px; }
  .arrow { position: absolute; left: 300px; top: 1000px; width: 225px; height: 122px; }
</style>
</head>
<body>
<main class="flyer">
  <svg class="backdrop" width="847" height="1200" viewBox="0 0 847 1200" aria-hidden="true">
    <defs>
      <linearGradient id="meadow" x1="0" y1="0" x2="0" y2="1">
        <stop offset="0" stop-color="#ffffff"/>
        <stop offset="0.45" stop-color="#d8f0b4"/>
        <stop offset="1" stop-color="#6cc41c"/>
      </linearGradient>
    </defs>
    <path d="M0 760 C 250 720, 600 640, 847 600 L847 1200 L0 1200 Z" fill="url(#meadow)"/>
    <path d="M380 1200 C 560 1120, 720 1090, 847 1080 L847 1200 Z" fill="#ffffff" opacity="0.85"/>
  </svg>

  <div class="top-band"></div>

  <p class="copy intro">We have vans in all sizes including Luton tail lifts for short and long term rental<br>on flexible terms for any purpose at very competitive prices.</p>

  <div class="banner banner-call">
    <svg width="811" height="82" viewBox="0 0 811 82" aria-hidden="true">
      <defs>
        <linearGradient id="pill-a" x1="0" y1="0" x2="0" y2="1">
          <stop offset="0" stop-color="#93c782"/>
          <stop offset="1" stop-color="#4f8f45"/>
        </linearGradient>
      </defs>
      <path d="M40 4 H560 C 600 4, 610 0, 640 0 H811 V12 H650 C 620 12, 610 16, 600 30 L590 60 C 584 76, 572 80, 550 80 H40 C 18 80, 2 62, 2 42 C 2 22, 18 4, 40 4 Z" fill="url(#pill-a)" stroke="#3d6f35" stroke-width="2"/>
    </svg>
    <p class="banner-text">When you need a van for business<br>purposes give Brenwick a call first.</p>
  </div>

  <p class="copy lead">We supply vans to businesses throughout Herts and Essex from large blue chip<br>multinationals to small self employed tradesman. We understand the<br>requirements of business customers and provide a low cost, flexible, efficient<br>van hire solution regardless of the size of your business.</p>

  <section class="point point-price">
    <svg class="point-icon" viewBox="0 0 46 26" aria-hidden="true"><rect x="1" y="7" width="20" height="14" rx="2" fill="#6f7f6a"/><rect x="22" y="2" width="22" height="22" rx="3" fill="#6f7f6a"/><path d="M27 13 l5 6 l10 -14" stroke="#fff" stroke-width="3.5" fill="none" stroke-linecap="round"/></svg>
    <h2 class="point-title">We’re cheaper than the rest</h2>
    <p class="point-body">We regularly search the market to ensure our pricing is always competitive.<br>It's important to us to give you excellent value for money.<br>We operate a clear pricing structure with no hidden extras.<br>Call us now and let us give you a quote.</p>
  </section>

  <section class="point point-term">
    <svg class="point-icon" viewBox="0 0 46 26" aria-hidden="true"><rect x="1" y="7" width="20" height="14" rx="2" fill="#6f7f6a"/><rect x="22" y="2" width="22" height="22" rx="3" fill="#6f7f6a"/><path d="M27 13 l5 6 l10 -14" stroke="#fff" stroke-width="3.5" fill="none" stroke-linecap="round"/></svg>
    <h2 class="point-title">Short or long term van hire</h2>
    <p class="point-body">We can supply vans according to your needs from just a single days<br>rental to long term contract rental for 1 month, 6 months, a whole year or more.</p>
  </section>

  <section class="point point-service">
    <svg class="point-icon" viewBox="0 0 46 26" aria-hidden="true"><rect x="1" y="7" width="20" height="14" rx="2" fill="#6f7f6a"/><rect x="22" y="2" width="22" height="22" rx="3" fill="#6f7f6a"/><path d="M27 13 l5 6 l10 -14" stroke="#fff" stroke-width="3.5" fill="none" stroke-linecap="round"/></svg>
    <h2 class="point-title">Committed to Customer service</h2>
    <p class="point-body">We take customer service very seriously. We want you to be delighted<br>each and every time you use us. That’s why We’ll always go out of our<br>way to give you a first class service.</p>
  </section>

  <div class="banner banner-discount">
    <svg width="811" height="82" viewBox="0 0 811 82" aria-hidden="true">
      <path d="M40 4 H560 C 600 4, 610 0, 640 0 H811 V12 H650 C 620 12, 610 16, 600 30 L590 60 C 584 76, 572 80, 550 80 H40 C 18 80, 2 62, 2 42 C 2 22, 18 4, 40 4 Z" fill="url(#pill-a)" stroke="#3d6f35" stroke-width="2"/>
    </svg>
    <p class="banner-text">The longer you hire the cheaper it gets with<br>discounts of up to 70% on our daily rental rates.</p>
  </div>

  <h1 class="tagline"><em>Affordable</em> &amp; <em>Flexible</em><br>van hire solutions<br>from Brenwick</h1>

  <p class="address">42 Tanwell Court, Harlow,<br>Essex, CM17 2QT</p>
  <p class="phone">0800 06 317 94</p>
  <p class="website">www.brenwickvanhire.example</p>

  <div class="map" role="img" aria-label="Street map showing the Brenwick depot in the foxmead industrial estate, Harlow"></div>
  <p class="gps">GPS: +51° 46' 12.08", +0° 6' 41.52”</p>

  <svg class="arrow" viewBox="0 0 225 122" aria-hidden="true">
    <path d="M6 112 C 60 72, 118 56, 170 50 L164 28 L222 50 L168 90 L170 70 C 120 74, 72 88, 30 120 Z" fill="#f5f000" stroke="#d8d200" stroke-width="1.5"/>
  </svg>
</main>
</body>
</html>
```